Business Card Design Project

I require a business card design that looks professional for a small building company. Calloway Builders is the name of the company and i don't want to use a house or building design for a logo. I require a logo design for the card incorporating the name Calloway Builders but designed smartly.

We are a Registered Building Practitioner so the small logo attached must also be used on the card.

We cover a large range of Building / Construction, Concrete, Steelwork. Not sure how to implement this.

Colors are flexible, maybe a dark grey background with white writting over it, but i am keen to see other options.

Thanks.

Target Market(s)

Anyone

Industry/Entity Type

Building

Requirements
Must have
• The logo attached must be incorporated - can be small
A logo for my company needs to be included - using Calloway Builders as the base with no picture of a house or buildings.

```html
<!DOCTYPE html>
<html lang="en">
<head>
<meta charset="utf-8">
<title>Calloway Builders — Business Cards</title>
<link rel="stylesheet" href="https://fonts.googleapis.com/css2?family=Michroma&display=swap">
<style>
  :root {
    --bg: #2b2b2b;
    --card-blue: #123e7c;
    --card-blue-deep: #0c2d5e;
    --band: #1f1f22;
    --white: #ffffff;
    --muted: #d7e0ee;
  }
  * { margin: 0; padding: 0; box-sizing: border-box; }
  html, body { width: 1200px; height: 900px; overflow: hidden; }
  body {
    background: var(--bg);
    font-family: "Michroma", "Arial", sans-serif;
    color: var(--white);
    position: relative;
  }
  .card {
    position: absolute;
    left: 280px;
    width: 640px;
    height: 366px;
    background: linear-gradient(135deg, var(--card-blue) 0%, var(--card-blue-deep) 100%);
    overflow: hidden;
  }
  .card--back { top: 70px; }
  .card--front { top: 464px; }

  .wordmark {
    position: absolute;
    display: flex;
    align-items: center;
    gap: 10px;
    text-transform: uppercase;
    line-height: 0.95;
    color: var(--white);
    white-space: nowrap;
  }
  .wordmark__mark {
    width: 0.8em;
    height: 0.8em;
    background: var(--white);
    flex: none;
  }
  .wordmark__name span { display: block; }

  /* back card */
  .card--back .wordmark { left: 52px; top: 66px; font-size: 26px; }
  .registered-badge {
    position: absolute;
    left: 380px;
    top: 72px;
    width: 34px;
    height: 34px;
    border: 2px solid var(--muted);
    border-radius: 50%;
  }
  .name-band {
    position: absolute;
    left: 0;
    top: 150px;
    width: 380px;
    height: 32px;
    background: var(--band);
    display: flex;
    align-items: center;
    padding-left: 52px;
    font-size: 14px;
    letter-spacing: 0.5px;
    text-transform: uppercase;
    white-space: nowrap;
  }
  .contact {
    position: absolute;
    left: 52px;
    top: 194px;
    font-size: 10px;
    line-height: 1.75;
    letter-spacing: 0.4px;
    color: var(--white);
    text-transform: uppercase;
    white-space: nowrap;
  }
  .contact__role { margin-bottom: 12px; }
  .contact__label { color: var(--muted); margin-right: 4px; }

  /* front card */
  .card--front .wordmark { left: 108px; top: 96px; font-size: 44px; }
  .services-band {
    position: absolute;
    left: 0;
    top: 228px;
    width: 100%;
    height: 36px;
    background: var(--band);
    display: flex;
    align-items: center;
    justify-content: center;
    font-size: 12px;
    letter-spacing: 1px;
    text-transform: uppercase;
    white-space: nowrap;
  }
  .services-band .sep { margin: 0 10px; }
  .website {
    position: absolute;
    left: 0;
    top: 290px;
    width: 100%;
    text-align: center;
    font-size: 13px;
    letter-spacing: 2px;
    text-transform: uppercase;
  }
</style>
</head>
<body>
  <section class="card card--back">
    <div class="wordmark">
      <div class="wordmark__name"><span>Calloway</span><span>Builders</span></div>
      <div class="wordmark__mark"></div>
    </div>
    <div class="registered-badge" role="img" aria-label="Registered building practitioner badge"></div>
    <div class="name-band">Marisol Keane R.</div>
    <div class="contact">
      <p class="contact__role">Licensed Plumber</p>
      <p>Address 48 Harbor Rd. 2210 Linden, Oakvale CA 90210</p>
      <p><span class="contact__label">P.</span>555 0142 760 <span class="contact__label">F.</span>555 0142 760</p>
      <p><span class="contact__label">E.</span>marisol@callowaybuilders.com</p>
      <p>www.callowaybuilders.com</p>
    </div>
  </section>

  <section class="card card--front">
    <div class="wordmark">
      <div class="wordmark__name"><span>Calloway</span><span>Builders</span></div>
      <div class="wordmark__mark"></div>
    </div>
    <div class="services-band">
      Building<span class="sep">|</span>Construction<span class="sep">|</span>Concrete<span class="sep">|</span>Steelwork
    </div>
    <p class="website">www.callowaybuilders.com</p>
  </section>
</body>
</html>
```